Design required for boutique fire engineering firm in New Zealand

Our website was published based on free Wordpress templates, we'd like something a bit more bespoke, clean and simple.
Updates

Reason: didn't check this finished on a Sunday :)

Target Market(s)

architects, building owners, property developers

Industry/Entity Type

Boutique

Contact Information for Business Card

Logo
Fire Engineering

Desmond Harlow
Principal
+64 21 482 735
desmond@veltrane.nz
veltrane.nz

Number of Pages Required

3 page

Font styles to use
Sans Serif

Requirements
Nice to have
• On the business card, an embossed logo would be great - not sure if that's a design thing or just a print thing?
• Website, existing @ http://veltrane.nz for extent of content and general arrangement that I'm happy with.
• Ability to update the content with project bio's and some photos at a later date would be nice.

```html
<!DOCTYPE html>
<html lang="en">
<head>
<meta charset="utf-8">
<title>Veltrane — Fire Engineering</title>
<link rel="stylesheet" href="https://fonts.googleapis.com/css2?family=Open+Sans:wght@400;600;700&display=swap">
<style>
:root{
  --navy:#1b4f7c;
  --blue:#2e6fb0;
  --orange:#ff4b12;
  --ink:#2b2b2b;
  --band:#f1f0ee;
  --dark:#1d0e08;
  --footer:#2b1b13;
  --white:#ffffff;
}
*{box-sizing:border-box;margin:0;padding:0}
html,body{width:1200px;height:2350px;overflow:hidden}
body{position:relative;font-family:"Open Sans",Arial,sans-serif;color:var(--ink);background:var(--white)}
.abs{position:absolute}

/* hero */
.hero{left:0;top:0;width:1200px;height:580px;background:radial-gradient(ellipse at 70% 40%,#f3a23a 0%,#d9581a 35%,#7a1f08 75%,#3a0d04 100%)}
.hero-figure{left:560px;top:0;width:560px;height:580px;background:linear-gradient(180deg,#6b3a1c 0%,#c4792a 45%,#3a1a0c 100%);opacity:.55}
.social-top{top:12px;right:150px;display:flex;gap:12px}
.dot{width:14px;height:14px;border-radius:3px;background:var(--white)}
.navbar{left:0;top:34px;width:1200px;height:65px;background:rgba(255,255,255,.88)}
.brand{display:flex;align-items:center;gap:10px;font-weight:700;color:var(--navy);font-size:34px;letter-spacing:-.5px}
.brand .mark{width:32px;height:32px;border-radius:50%;background:var(--navy)}
.nav-brand{left:149px;top:45px}
.nav{top:58px;left:641px;font-size:15px;font-weight:600;color:#333}
.nav a{color:inherit;text-decoration:none;position:absolute;white-space:nowrap}
.nav a.active{color:var(--navy);font-weight:700}
.search{left:1034px;top:60px}
.hero-caption{left:149px;top:251px;width:650px;height:169px;background:rgba(150,25,5,.55)}
.hero-title{left:40px;top:14px;font-size:60px;color:var(--white);font-weight:400;letter-spacing:1px}
.hero-sub{left:46px;top:98px;font-size:42px;color:var(--white);font-weight:400}
.slide-btn{left:149px;width:41px;height:44px;display:flex;align-items:center;justify-content:center}
.slide-next{top:453px;background:var(--blue)}
.slide-prev{top:506px;background:rgba(150,90,50,.7)}

/* headings */
.section-title{width:1200px;left:0;text-align:center;color:var(--navy);font-weight:600;font-size:37px}

/* services */
.service-icon{width:40px;height:44px}
.service-card{top:788px;width:169px;height:180px;background:var(--white);border:2px solid #e3e3e3;box-shadow:0 1px 3px rgba(0,0,0,.08);text-align:center}
.service-card h3{margin-top:14px;font-size:14px;font-weight:700;color:var(--blue);line-height:21px;padding:0 6px}
.service-card p{margin-top:8px;font-size:12px;line-height:17px;color:#333;padding:0 12px}
.tag-btn{position:absolute;background:var(--orange);color:var(--white);clip-path:polygon(0 0,100% 0,78% 100%,0 100%)}
.service-card .tag-btn{left:0;bottom:8px;width:100px;height:23px;font-size:8px;line-height:23px;padding-left:12px;text-align:left}

/* fire band */
.band{left:0;top:1026px;width:1200px;height:381px;background:var(--band)}
.band-title{left:149px;top:1088px;font-size:37px;font-weight:600;color:var(--navy);white-space:nowrap}
.band-copy{left:149px;top:1167px;width:501px;font-size:12.4px;line-height:17px;text-align:justify;color:#333}
.learn-btn{left:149px;top:1321px;width:141px;height:35px;font-size:13px;line-height:35px;padding-left:18px}
.band-image{left:650px;top:1070px;width:400px;height:315px;background:radial-gradient(ellipse 45% 48% at 68% 55%,#e23a2a 0%,#c4261a 40%,rgba(241,240,238,0) 100%)}

/* testimonials */
.quote-card{top:1658px;width:279px;height:257px;background:var(--dark)}
.quote-card p{position:absolute;left:31px;top:70px;width:230px;font-size:13.5px;line-height:23.5px;color:#f2f2f2}
.quote-card .tag-btn{left:0;top:202px;width:160px;height:38px;font-size:14px;line-height:38px;padding-left:20px}
.avatar{top:1547px;width:150px;height:150px;border-radius:50%;border:3px solid var(--orange);background:linear-gradient(180deg,#d9c2ae,#9a7e68)}
.chev{top:1760px}

/* footer */
.footer{left:0;top:1995px;width:1200px;height:318px;background:linear-gradient(90deg,#2a1a12,#3a2417 50%,#2a1a12)}
.footer-brand{left:149px;top:2037px}
.footer-brand.brand{font-size:32px;color:var(--blue)}
.footer-brand .mark{background:var(--blue)}
.foot-links{left:149px;top:2108px;list-style:none;font-size:15px;color:var(--white)}
.foot-links li{height:36px}
.foot-head{font-size:19px;color:var(--orange);font-weight:400}
.foot-text{font-size:15px;color:var(--white);line-height:36.5px}
.newsletter{left:809px;top:2097px;width:241px;height:34px;border:1px solid #9a8a80;display:flex}
.newsletter span{flex:1;font-size:12px;color:#bbb;padding:8px 9px}
.newsletter b{width:68px;border-left:1px solid #9a8a80;color:var(--white);font-weight:400;font-size:13px;text-align:center;line-height:32px}
.foot-social{left:812px;top:2256px;display:flex;gap:27px}
.copyright{left:0;top:2313px;width:1200px;height:37px;background:var(--orange);color:var(--white);font-size:8px;text-align:center;line-height:37px}
</style>
</head>
<body>

<section class="hero abs" role="img" aria-label="Firefighter in protective gear walking into a wall of flames"></section>
<div class="hero-figure abs" role="img" aria-label="Firefighter with breathing apparatus seen from behind"></div>

<div class="social-top abs" aria-label="Social links"><span class="dot"></span><span class="dot"></span></div>

<header class="navbar abs"></header>
<div class="brand nav-brand abs"><span class="mark"></span>veltrane</div>
<nav class="nav abs">
  <a class="active" href="#" style="left:0">Home</a>
  <a href="#" style="left:88px">About us</a>
  <a href="#" style="left:179px">Services</a>
  <a href="#" style="left:269px">Contact Us</a>
</nav>
<svg class="search abs" width="18" height="18" viewBox="0 0 18 18" aria-label="Search"><circle cx="7.5" cy="7.5" r="5.5" fill="none" stroke="#444" stroke-width="1.6"/><line x1="11.5" y1="11.5" x2="16" y2="16" stroke="#444" stroke-width="1.6"/></svg>

<div class="hero-caption abs">
  <h1 class="hero-title abs">FIRE ENGINEERING</h1>
  <p class="hero-sub abs">thoughtful, responsive</p>
</div>
<div class="slide-btn slide-next abs"><svg width="10" height="12" viewBox="0 0 10 12"><path d="M3 2l4 4-4 4" fill="none" stroke="#fff" stroke-width="1.5"/></svg></div>
<div class="slide-btn slide-prev abs"><svg width="10" height="12" viewBox="0 0 10 12"><path d="M7 2L3 6l4 4" fill="none" stroke="#d8b7a0" stroke-width="1.5"/></svg></div>

<h2 class="section-title abs" style="top:612px">Our Services</h2>

<svg class="service-icon abs" style="left:245px;top:712px" viewBox="0 0 40 44" aria-label="Flame"><path d="M20 2c2 8 12 12 12 24a12 12 0 0 1-24 0c0-6 3-9 5-12 0 5 2 7 4 7-2-7 1-13 3-19z" fill="var(--orange)"/><path d="M20 24c1 4 5 5 5 10a5 5 0 0 1-10 0c0-3 3-5 5-10z" fill="#fff"/></svg>
<svg class="service-icon abs" style="left:465px;top:712px;width:50px" viewBox="0 0 50 44" aria-label="Helmet"><path d="M6 28c0-12 8-20 19-20s19 8 19 20z" fill="var(--orange)"/><rect x="2" y="28" width="46" height="6" rx="3" fill="var(--orange)"/><rect x="21" y="12" width="8" height="12" fill="#fff"/></svg>
<svg class="service-icon abs" style="left:692px;top:710px" viewBox="0 0 40 44" aria-label="Hydrant"><rect x="12" y="4" width="16" height="6" rx="2" fill="var(--orange)"/><rect x="10" y="10" width="20" height="30" fill="var(--orange)"/><rect x="3" y="18" width="34" height="10" rx="2" fill="var(--orange)"/><rect x="16" y="14" width="3" height="22" fill="#fff"/><rect x="22" y="14" width="3" height="22" fill="#fff"/></svg>
<svg class="service-icon abs" style="left:918px;top:710px" viewBox="0 0 40 44" aria-label="Alarm"><circle cx="20" cy="28" r="12" fill="var(--orange)"/><circle cx="20" cy="28" r="6" fill="#fff"/><circle cx="20" cy="28" r="3" fill="var(--orange)"/><path d="M24 8a10 10 0 0 1 10 10" fill="none" stroke="var(--orange)" stroke-width="3"/><path d="M24 2a16 16 0 0 1 16 16" fill="none" stroke="var(--orange)" stroke-width="3"/></svg>

<article class="service-card abs" style="left:171px"><h3>FIRE PREVENTION</h3><p style="margin-top:24px">Lorem Ipsum is simply dummy text of the printing and typesetting industry.Primers....</p><span class="tag-btn">Read More</span></article>
<article class="service-card abs" style="left:398px"><h3>DEPARTMENT INFORMATION</h3><p>Lorem Ipsum is simply &nbsp;and typesetting industry.Primers....</p><span class="tag-btn">Read More</span></article>
<article class="service-card abs" style="left:627px"><h3>PUBLIC EDUCATION</h3><p style="margin-top:24px">Lorem Ipsum is simply dummy text of the printing and typesetting industry.Primers....</p><span class="tag-btn">Read More</span></article>
<article class="service-card abs" style="left:854px"><h3>FSTRATEGIC PLAN</h3><p style="margin-top:4px">Lorem Ipsum is simply dummy text of the printing and typesetting industry.Primers....</p><span class="tag-btn">Read More</span></article>

<section class="band abs"></section>
<div class="band-image abs" role="img" aria-label="Red fire extinguisher in front of a blurred fire truck"></div>
<h2 class="band-title abs">Think of fire before it statrs</h2>
<p class="band-copy abs">It is a long established fact that a reader will be distracted by the readable content of a page when looking at its layout. The point of using Lorem Ipsum is that it has a more-or-less normal distribution of letters, as opposed to using 'Content here, content here', making it look like readable English. Many desktop publishing packages and web page editors now use Lorem Ipsum as their default model text, and a search for 'lorem ipsum' will uncover many web sites still in their infancy. Various versions have evolved over the years, sometimes by accident, sometimes on purpose (injected humour and the like).</p>
<span class="tag-btn learn-btn">Learn More</span>

<h2 class="section-title abs" style="top:1455px">They Say</h2>
<svg class="chev abs" style="left:96px" width="22" height="40" viewBox="0 0 22 40"><path d="M18 4L4 20l14 16" fill="none" stroke="#b9cde0" stroke-width="3"/></svg>
<svg class="chev abs" style="left:1076px" width="22" height="40" viewBox="0 0 22 40"><path d="M4 4l14 16L4 36" fill="none" stroke="#b9cde0" stroke-width="3"/></svg>

<article class="quote-card abs" style="left:149px"><p>Lorem Ipsum is simply dummy te d dum centuries, but also the leap into electronic typesetting, remaining essentially unchanged.</p><span class="tag-btn">Read More</span></article>
<article class="quote-card abs" style="left:461px"><p>Lorem Ipsum is simply dummy te d dum centuries, but also the leap into electronic typesetting, remaining essentially unchanged.</p><span class="tag-btn">Read More</span></article>
<article class="quote-card abs" style="left:772px"><p>Lorem Ipsum is simply dummy te d dum centuries, but also the leap into electronic typesetting, remaining essentially unchanged.</p><span class="tag-btn">Read More</span></article>
<div class="avatar abs" style="left:221px" role="img" aria-label="Client portrait"></div>
<div class="avatar abs" style="left:533px" role="img" aria-label="Client portrait"></div>
<div class="avatar abs" style="left:845px" role="img" aria-label="Client portrait"></div>

<footer class="footer abs" role="img" aria-label="Dark backdrop of firefighters at a scene"></footer>
<div class="brand footer-brand abs"><span class="mark"></span>veltrane</div>
<ul class="foot-links abs"><li>Home</li><li>About us</li><li>Our services</li><li>They say</li><li>Contact Us</li></ul>

<h4 class="foot-head abs" style="left:461px;top:2042px">Address</h4>
<p class="foot-text abs" style="left:461px;top:2075px">Lorem Ipsum is simply dummy<br>text of the printing<br>and typesetting industry.</p>
<h4 class="foot-head abs" style="left:461px;top:2213px">Phone</h4>
<p class="foot-text abs" style="left:461px;top:2246px">098310 47215</p>

<h4 class="foot-head abs" style="left:810px;top:2042px">Newsletter</h4>
<div class="newsletter abs"><span>Email</span><b>GO</b></div>
<h4 class="foot-head abs" style="left:810px;top:2214px">Get in touch with us</h4>
<div class="foot-social abs"><span class="dot"></span><span class="dot"></span></div>

<div class="copyright abs">©copyright 2017 All Rights Reserved</div>

</body>
</html>
```